Webbanner-Design für Startseite im Online-Shop
Zielgruppe
Wir sind ein Fachhandel für Nähmaschinen, Stickmaschinen und Zubehör.
Unsere Zielgruppe sind hauptsächlich nähbegeisterte Frauen.
Aufgabenstellung
Wir möchten den Werbebanner für unsere Startseite im Onlineshop und als Popup verwenden. Das ganze soll eine Eintauschaktion werden. Die alte Overlock antauschen und diese neue Overlock zum Sonderpreis erhalten. Hier der Text für den Banner.
ALTE OVERLOCK TAUSCHEN GEGEN EINE NEUE
Hier noch unser Shop, damit man es etwas anpassen kann.
Stoffwerk-Laden.de
Hier ca. die Größe des Banners.
Breite: 2000 Pixel
Höhe: 1071 Pixel
Bei weiteren Fragen könnt Ihr euch gerne bei mir melden.
Viele Grüße
Matthias Lohberg

```html
<!DOCTYPE html>
<html lang="de">
<head>
<meta charset="utf-8">
<title>Eintauschaktion Overlock – Stoffwerk-Laden</title>
<link rel="stylesheet" href="https://fonts.googleapis.com/css2?family=Archivo:ital,wdth,wght@0,62..125,400;0,62..125,700;0,62..125,900;1,62..125,900&display=swap">
<style>
  :root {
    --red: #d0103a;
    --black: #0b0b0b;
    --white: #ffffff;
    --stitch: #6f6f6f;
    --band-red-a: rgba(168, 24, 52, 0.86);
    --band-red-b: rgba(196, 60, 88, 0.78);
  }
  html, body { margin: 0; padding: 0; overflow: hidden; }
  body { width: 1200px; height: 643px; background: #fff; }
  .banner {
    position: relative; width: 1200px; height: 643px; overflow: hidden;
    font-family: "Archivo", "Helvetica Neue", Arial, sans-serif;
  }
  .photo { position: absolute; top: 0; height: 643px; }
  .photo--left {
    left: 0; width: 600px;
    background:
      radial-gradient(ellipse 260px 140px at 90px 330px, rgba(40,40,44,0.75), transparent 70%),
      radial-gradient(ellipse 220px 160px at 250px 120px, rgba(226,222,200,0.9), transparent 70%),
      radial-gradient(ellipse 260px 200px at 480px 60px, rgba(150,110,70,0.7), transparent 70%),
      radial-gradient(ellipse 300px 160px at 220px 560px, rgba(150,80,60,0.8), transparent 70%),
      linear-gradient(170deg, #b9ae92 0%, #cfcab8 40%, #c9c5b6 65%, #9c6e58 100%);
  }
  .photo--right {
    left: 600px; width: 600px;
    background:
      radial-gradient(ellipse 220px 240px at 440px 150px, rgba(255,255,255,0.95), transparent 70%),
      radial-gradient(ellipse 200px 140px at 60px 80px, rgba(200,196,186,0.9), transparent 70%),
      radial-gradient(ellipse 220px 160px at 80px 580px, rgba(120,96,84,0.7), transparent 70%),
      radial-gradient(ellipse 160px 90px at 560px 200px, rgba(140,110,80,0.5), transparent 70%),
      linear-gradient(190deg, #e6e3dc 0%, #f3f2ef 45%, #e4e2de 75%, #b8b0a8 100%);
  }
  .headline-band {
    position: absolute; left: 0; top: 126px; width: 1200px; height: 333px;
    background: linear-gradient(90deg, rgba(255,255,255,0.3) 0%, rgba(255,255,255,0.78) 26%, rgba(255,255,255,0.86) 70%, rgba(255,255,255,0.35) 100%);
  }
  .headline {
    position: absolute; margin: 0; font-style: italic; font-weight: 900;
    font-stretch: 125%; line-height: 1; white-space: nowrap;
  }
  .headline--old { left: 324px; top: 154px; font-size: 61px; letter-spacing: 0.6px; color: var(--red); }
  .headline--swap { left: 299px; top: 262px; font-size: 60px; letter-spacing: 0.7px; color: var(--black); }
  .headline--new { left: 423px; top: 370px; font-size: 61px; letter-spacing: 1.6px; color: var(--red); }
  .stitch-arrows { position: absolute; left: 0; top: 0; width: 1200px; height: 643px; }
  .stitch-strip { position: absolute; height: 20px; }
  .stitch-strip--upper { left: 362px; top: 226px; width: 541px; }
  .stitch-strip--lower { left: 294px; top: 334px; width: 541px; }
  .stitch-strip__fill {
    position: absolute; inset: 3px 0 3px 0;
    background: linear-gradient(180deg, rgba(90,90,90,0.35), rgba(90,90,90,0.55));
  }
  .stitch-strip__edge { position: absolute; left: 0; right: 0; height: 1px; background: var(--black); }
  .stitch-strip--upper .stitch-strip__edge { top: 0; }
  .stitch-strip--lower .stitch-strip__edge { bottom: 0; }
  .price-badge {
    position: absolute; left: 795px; top: 370px; width: 162px; height: 76px;
    border-radius: 50%; background: var(--red); transform: rotate(-12deg);
    color: var(--white); text-align: center; font-stretch: 85%;
  }
  .price-badge span { display: block; line-height: 1; font-weight: 400; }
  .price-badge .small { font-size: 16px; margin-top: 14px; }
  .price-badge .big { font-size: 20px; margin-top: 3px; }
  .footer-band {
    position: absolute; left: 0; top: 503px; width: 1200px; height: 140px;
    background: linear-gradient(90deg, var(--band-red-b) 0%, var(--band-red-a) 55%, rgba(200,150,160,0.7) 100%);
  }
  .shop-url {
    position: absolute; left: 183px; top: 535px; margin: 0;
    font-weight: 700; font-stretch: 108%; font-size: 56px; color: var(--white);
    line-height: 1; white-space: nowrap;
  }
  .shop-name {
    position: absolute; left: 907px; top: 540px; width: 246px; height: 56px;
  }
  .shop-name__text {
    position: absolute; left: 0; top: 0;
    font-weight: 900; font-stretch: 112%; color: var(--red);
    font-size: 27px; line-height: 0.98; white-space: nowrap;
  }
  .shop-name__mark {
    position: absolute; right: 0; bottom: 2px; width: 38px; height: 38px; background: var(--red);
  }
</style>
</head>
<body>
  <section class="banner">
    <div class="photo photo--left" role="img" aria-label="Industrienähmaschine mit dunklem Stoff und Schere auf der Arbeitsplatte"></div>
    <div class="photo photo--right" role="img" aria-label="Weiße Nähmaschine mit Nähfuß in Nahaufnahme"></div>

    <div class="headline-band"></div>

    <div class="stitch-strip stitch-strip--upper" role="img" aria-label="Zickzack-Naht">
      <div class="stitch-strip__fill"></div><div class="stitch-strip__edge"></div>
    </div>
    <div class="stitch-strip stitch-strip--lower" role="img" aria-label="Zickzack-Naht">
      <div class="stitch-strip__fill"></div><div class="stitch-strip__edge"></div>
    </div>

    <svg class="stitch-arrows" viewBox="0 0 1200 643" aria-hidden="true">
      <line x1="340" y1="236" x2="364" y2="236" stroke="#0b0b0b" stroke-width="6"/>
      <polygon points="294,236 350,214 338,236 350,258" fill="#0b0b0b"/>
      <line x1="833" y1="344" x2="858" y2="344" stroke="#0b0b0b" stroke-width="6"/>
      <polygon points="903,344 849,322 861,344 849,366" fill="#0b0b0b"/>
    </svg>

    <h1 class="headline headline--old">ALTE OVERLOCK</h1>
    <p class="headline headline--swap">TAUSCHEN GEGEN</p>
    <p class="headline headline--new">EINE NEUE</p>

    <div class="price-badge">
      <span class="small">zum</span>
      <span class="big">SONDERPREIS</span>
    </div>

    <div class="footer-band"></div>
    <p class="shop-url">www.Stoffwerk-Laden.de</p>
    <div class="shop-name">
      <div class="shop-name__text">STOFFWERK<br>LADEN</div>
      <div class="shop-name__mark"></div>
    </div>
  </section>
</body>
</html>
```